Brook Hollow Patio In-Store Brochure

We sell bbq's, hot tubs, fireplaces, firepits... our company is at www.brookhollowpatio.example . We would like the brochure to highlight some of our best brands (Ember, HeatCraft, TWR, Corvan, DKT & Ventaro grills / Halden BBQ Equipment / Coastal Kindle Works, Brevanto, Stalwick, Parkhurst fireplace / Tidewell Spas (Hot Tubs) / etc. see website!)

Target Market(s)

To give out to people when they come in to the store

Industry/Entity Type

It Company

Requirements
Must have
• An "About Us" section, show the manufacturers/brands that we deal with, have something about the 3 categories we sell to (BBQ/BBQ Equipment/ BBQ Islands.... Hot Tubs by Tidewell Spas..... Fireplaces / Firepits / Fireplace Media ).
Nice to have
• Website, phone, address, email, About Us, Brands that we deal with, etc.

```html
<!DOCTYPE html>
<html lang="en">
<head>
<meta charset="utf-8">
<title>Brook Hollow Patio – In-Store Brochure</title>
<link rel="stylesheet" href="https://fonts.googleapis.com/css2?family=Cinzel:wght@400;600&family=Open+Sans:ital,wght@0,400;0,600;0,700;1,600&display=swap">
<style>
  :root {
    --red: #b3141c;
    --red-dark: #7a0b10;
    --ink: #1b1b1b;
    --text: #4a4a4a;
    --paper: #ffffff;
    --paper-shade: #ececec;
    --stage: #dedede;
    --stone: #8a7560;
    --wood: #7a3f22;
    --steel: #b9bcbf;
  }
  * { box-sizing: border-box; margin: 0; padding: 0; }
  html, body { width: 1200px; height: 2400px; overflow: hidden; }
  body { background: var(--stage); font-family: "Open Sans", Arial, sans-serif; color: var(--text); position: relative; }

  .spread { position: absolute; left: 60px; width: 1080px; height: 834px; display: flex; box-shadow: 0 18px 40px rgba(0,0,0,.22); }
  .spread--outside { top: 270px; }
  .spread--inside { top: 1296px; }

  .panel { position: relative; width: 360px; height: 834px; overflow: hidden;
    background: linear-gradient(180deg, var(--paper) 0%, var(--paper) 55%, var(--paper-shade) 100%); }
  .panel + .panel { border-left: 1px solid #d6d6d6; }
  .panel svg.band { position: absolute; left: 0; width: 360px; display: block; }

  /* name block */
  .brand { display: flex; align-items: center; justify-content: center; gap: 12px; }
  .brand__mark { width: 22px; height: 22px; background: var(--ink); flex: none; }
  .brand__name { font-weight: 700; font-size: 27px; color: var(--ink); letter-spacing: .5px; line-height: 1.1; }

  .photo { position: absolute; left: 0; width: 100%; }

  /* about panel */
  .about { padding: 46px 30px 0 34px; }
  .about__title { font-family: "Cinzel", Georgia, serif; font-weight: 600; color: var(--red); font-size: 22px; letter-spacing: 1px; margin-bottom: 12px; }
  .about__text { font-size: 12.5px; line-height: 1.55; margin-bottom: 12px; }
  .brand-list { list-style: none; font-size: 12.5px; line-height: 1.6; margin-bottom: 14px; }
  .brand-list li { padding-left: 16px; position: relative; }
  .brand-list li::before { content: ""; position: absolute; left: 2px; top: 8px; width: 6px; height: 6px; border-radius: 50%; background: var(--red); }
  .about__tagline { color: var(--red); font-style: italic; font-weight: 600; font-size: 12.5px; line-height: 1.45; }
  .about__curve { position: absolute; top: 0; left: 0; }
  .about__photo { bottom: 0; height: 220px; background: linear-gradient(120deg, #1d2f6b 0%, #9b1b24 45%, #e9e2d6 60%, #6b4a2b 100%); }
  .estimate { position: absolute; left: 0; bottom: 0; width: 100%; height: 34px; background: var(--ink); color: #fff; font-family: "Cinzel", Georgia, serif; font-size: 14px; letter-spacing: 2px; display: flex; align-items: center; justify-content: center; }

  /* back panel */
  .back .brand { margin-top: 64px; }
  .back__rule { height: 3px; width: 260px; margin: 18px auto 0; background: var(--red); }
  .back__lead { margin: 34px 28px 0; text-align: center; color: var(--red); font-weight: 700; font-size: 19px; line-height: 1.35; }
  .back__map { position: absolute; top: 400px; left: 90px; width: 180px; height: 180px; border-radius: 50%; border: 5px solid #fff; box-shadow: 0 3px 10px rgba(0,0,0,.2); background: radial-gradient(circle at 55% 45%, #f4f1ea 0%, #e3e0d7 60%, #cfd6c9 100%); }
  .back__contact { position: absolute; left: 0; top: 690px; width: 100%; text-align: center; color: #fff; font-size: 14px; line-height: 1.5; z-index: 2; }
  .back__phone { font-weight: 700; font-size: 17px; margin-top: 14px; }

  /* front cover */
  .cover .brand { margin-top: 70px; }
  .cover__photo { top: 200px; height: 420px; background:
    linear-gradient(180deg, rgba(122,63,34,.85) 0%, rgba(138,117,96,.7) 40%, rgba(185,188,191,.55) 60%, rgba(110,92,74,.95) 100%); }
  .cover__title { position: absolute; top: 640px; left: 0; width: 100%; text-align: center; z-index: 2; font-family: "Cinzel", Georgia, serif; color: #fff; font-size: 30px; line-height: 1.25; letter-spacing: 1px; }
  .cover__web { position: absolute; bottom: 0; left: 0; width: 100%; height: 52px; background: var(--ink); color: #fff; font-weight: 600; font-size: 15px; display: flex; align-items: center; justify-content: center; letter-spacing: .5px; z-index: 2; }

  /* inside panels */
  .category__photo { top: 0; height: 238px; }
  .category__photo--bbq { background: linear-gradient(160deg, #2f3b23 0%, #5e4b38 50%, #9a8d7c 100%); }
  .category__photo--spa { background: linear-gradient(160deg, #3a2616 0%, #8a5a2f 45%, #d8b98a 100%); }
  .category__photo--fire { background: linear-gradient(160deg, #2e4a2a 0%, #6d7f62 45%, #4c7fa6 100%); }
  .category__head { position: absolute; top: 220px; left: 0; width: 100%; height: 72px; }
  .category__title { position: absolute; top: 240px; left: 0; width: 100%; text-align: center; color: #fff; font-weight: 700; font-size: 19px; z-index: 2; }
  .category__body { position: absolute; top: 312px; left: 28px; right: 28px; font-size: 12.5px; line-height: 1.55; }
  .category__body p + p { margin-top: 10px; }
  .feature-list { list-style: none; margin-top: 10px; }
  .feature-list li { padding-left: 18px; position: relative; line-height: 1.7; }
  .feature-list li::before { content: ""; position: absolute; left: 0; top: 6px; width: 9px; height: 9px; border-radius: 50%; background: var(--red); }
  .thumbs { position: absolute; top: 650px; left: 28px; right: 28px; display: flex; gap: 12px; }
  .thumb { flex: 1; height: 92px; border: 3px solid #fff; box-shadow: 0 2px 6px rgba(0,0,0,.25); }
  .thumb--stone { background: linear-gradient(150deg, #5d6b48, #a39785); }
  .thumb--deck { background: linear-gradient(150deg, #6a4a2c, #b8a285); }
  .thumb--water { background: linear-gradient(150deg, #3d6d8f, #9db7c5); }
  .thumb--fire { background: linear-gradient(150deg, #3b3b3b, #c0652b); }
</style>
</head>
<body>

<!-- Outside: about flap, back panel, front cover -->
<section class="spread spread--outside">

  <article class="panel about">
    <svg class="about__curve" width="360" height="60" viewBox="0 0 360 60" aria-hidden="true">
      <path d="M0 0 H360 V8 C250 40 120 10 0 34 Z" fill="var(--red)"/>
      <path d="M0 40 C120 16 250 46 360 14" stroke="var(--red-dark)" stroke-width="2" fill="none"/>
    </svg>
    <h2 class="about__title">About Us</h2>
    <p class="about__text">Brook Hollow Patio is a direct source for contractors, builders and homeowners who want quality outdoor products. We carry grills, islands, spas and fire features from trusted makers, and our staff will help you plan a backyard that fits your space and budget.</p>
    <ul class="brand-list">
      <li>Ember, HeatCraft &amp; TWR Grills</li>
      <li>Corvan, DKT &amp; Ventaro Grills</li>
      <li>Halden BBQ Equipment</li>
      <li>Coastal Kindle Works Fire Features</li>
      <li>Brevanto &amp; Stalwick Fireplaces</li>
      <li>Parkhurst Fireplaces &amp; Inserts</li>
      <li>Tidewell Spas Hot Tubs</li>
    </ul>
    <p class="about__tagline">Come to Brook Hollow Patio and let us help make your outdoor living great looking!</p>
    <div class="photo about__photo" role="img" aria-label="Waving national flag with a bald eagle"></div>
    <div class="estimate">FREE ESTIMATE</div>
  </article>

  <article class="panel back">
    <div class="brand"><span class="brand__mark"></span><span class="brand__name">Brook Hollow Patio</span></div>
    <div class="back__rule"></div>
    <p class="back__lead">We've been here since 2000, helping our clients with big &amp; small outdoor projects. Let us help you, too!</p>
    <div class="back__map" role="img" aria-label="Street map showing the store location"></div>
    <svg class="band" style="top:640px" width="360" height="194" viewBox="0 0 360 194" aria-hidden="true">
      <path d="M0 30 C120 0 240 0 360 22 V194 H0 Z" fill="var(--red)"/>
      <path d="M0 24 C120 -6 240 -6 360 16" stroke="var(--red-dark)" stroke-width="3" fill="none"/>
    </svg>
    <div class="back__contact">
      <p>4120 Meadowline Road</p>
      <p>Unit "B" Cedar Falls, CA 90210</p>
      <p class="back__phone">Call Us Now: (555) 014-2290</p>
    </div>
  </article>

  <article class="panel cover">
    <div class="brand"><span class="brand__mark"></span><span class="brand__name">Brook Hollow Patio</span></div>
    <div class="photo cover__photo" role="img" aria-label="Stone outdoor kitchen island with a built-in stainless steel grill and wooden fence"></div>
    <svg class="band" style="top:570px" width="360" height="264" viewBox="0 0 360 264" aria-hidden="true">
      <path d="M0 50 C130 10 250 0 360 0 V264 H0 Z" fill="var(--red)"/>
      <path d="M0 42 C130 2 250 -8 360 -8" stroke="var(--red-dark)" stroke-width="3" fill="none"/>
    </svg>
    <h1 class="cover__title">Outdoor<br>Living Experience</h1>
    <div class="cover__web">www.brookhollowpatio.example</div>
  </article>
</section>

<!-- Inside: three product categories -->
<section class="spread spread--inside">

  <article class="panel category">
    <div class="photo category__photo category__photo--bbq" role="img" aria-label="Store showroom with BBQ grills and islands"></div>
    <svg class="category__head" viewBox="0 0 360 72" preserveAspectRatio="none" aria-hidden="true">
      <path d="M0 18 C120 0 240 0 360 10 V60 C240 52 120 52 0 72 Z" fill="var(--red)"/>
    </svg>
    <h3 class="category__title">BBQ's and BBQ Islands</h3>
    <div class="category__body">
      <p>We carry many brands of residential and commercial quality BBQ grills, from Ember and HeatCraft to TWR, Corvan and DKT. Choose built-in or freestanding units in stainless steel, with infrared burners and rotisserie systems.</p>
      <p>We choose to carry grills that have proven performance for many years. Our BBQ islands are built to order with stone, stucco or tile finishes.</p>
      <p>As we always say, let us save you time and money: buy quality, as it costs less in the long run.</p>
    </div>
    <div class="thumbs">
      <div class="thumb thumb--stone" role="img" aria-label="Stone BBQ island"></div>
      <div class="thumb thumb--deck" role="img" aria-label="Built-in grill on patio"></div>
    </div>
    <svg class="band" style="top:770px" width="360" height="64" viewBox="0 0 360 64" aria-hidden="true">
      <path d="M0 0 C120 30 240 30 360 8 V64 H0 Z" fill="var(--red)"/>
    </svg>
  </article>

  <article class="panel category">
    <div class="photo category__photo category__photo--spa" role="img" aria-label="Showroom with hot tubs on display"></div>
    <svg class="category__head" viewBox="0 0 360 72" preserveAspectRatio="none" aria-hidden="true">
      <path d="M0 10 C120 0 240 0 360 18 V72 C240 52 120 52 0 60 Z" fill="var(--red)"/>
    </svg>
    <h3 class="category__title">Hot Tubs (Spas)</h3>
    <div class="category__body">
      <p>Brook Hollow Patio offers jet powered hot tubs from Tidewell Spas, one of the most trusted makers of acrylic spas.</p>
      <p>Relax in your own backyard and enjoy warm water therapy that eases muscles and washes away the stress of the day.</p>
      <p>The ongoing commitment to innovative product development means every model delivers high performance.</p>
      <ul class="feature-list">
        <li>Energy efficient pumps</li>
        <li>Easy to program filtration</li>
        <li>Full foam insulation</li>
        <li>LED lighting</li>
      </ul>
    </div>
    <div class="thumbs">
      <div class="thumb thumb--water" role="img" aria-label="Hot tub on a deck"></div>
      <div class="thumb thumb--deck" role="img" aria-label="Hot tub interior seating"></div>
    </div>
    <svg class="band" style="top:770px" width="360" height="64" viewBox="0 0 360 64" aria-hidden="true">
      <path d="M0 8 C120 30 240 30 360 0 V64 H0 Z" fill="var(--red)"/>
    </svg>
  </article>

  <article class="panel category">
    <div class="photo category__photo category__photo--fire" role="img" aria-label="Backyard fire pit with lounge chairs by a pool"></div>
    <svg class="category__head" viewBox="0 0 360 72" preserveAspectRatio="none" aria-hidden="true">
      <path d="M0 18 C120 0 240 0 360 10 V60 C240 52 120 52 0 72 Z" fill="var(--red)"/>
    </svg>
    <h3 class="category__title">Fireplaces &amp; Firepits</h3>
    <div class="category__body">
      <p>Fireplaces and fire pits are an attractive way to add warmth to your yard. We offer models from Coastal Kindle Works, Brevanto, Stalwick and Parkhurst in gas and wood burning styles.</p>
      <p>Sometimes you have an idea in your head, or you have seen one you love. Bring us a photo and we will help you pick the right fire feature and media.</p>
      <p>We offer customization services so that your fire pit looks just right, and our team is glad to guide you.</p>
    </div>
    <div class="thumbs">
      <div class="thumb thumb--fire" role="img" aria-label="Outdoor gas fireplace"></div>
      <div class="thumb thumb--stone" role="img" aria-label="Stone fire pit on patio"></div>
    </div>
    <svg class="band" style="top:770px" width="360" height="64" viewBox="0 0 360 64" aria-hidden="true">
      <path d="M0 0 C120 30 240 30 360 8 V64 H0 Z" fill="var(--red)"/>
    </svg>
  </article>
</section>

</body>
</html>
```